Inspirational Card with Words of Wisdom to Give to Kids

I run basketball camps and give inspirational messages to elementary schools and high schools (www.brightpathcourts.com).

I would like to create a card that has some inspirational thoughts and words of wisdom on it that I can give away...and that students and athletes will keep in their wallet as a reminder of things I've taught them.

I want it to be clean and classy, while not looking too child-like or business-like, as I'd like to be able to give it out to kids, teenagers, and young adults.

The card will be the size of a regular business card and will be double-sided. I would like to use black, orange, gray, and white as the primary colors, with white or gray likely being the background color.
Updates

You're welcome to leave off the title "Lessons to Carry" if desired and just use "The Golden Compass of Growth" on the front of the card.

Thanks.

If you choose to leave off the poem, which you're welcome to do, please make one minor addition to the 5-point creed:

Add the words "God and" to "Honour others in everything you say and do" so it becomes:

"Honour God and others in everything you say and do."

Target Market(s)

Children, Teenagers, and Young Adults

Industry/Entity Type

Business

Requirements
Must have
• All the content, although the poem could be removed if necessary.
Should not have
• Nothing basketball-specific, as I want to be able to give it out to any child or teenager.

```html
<!DOCTYPE html>
<html lang="en">
<head>
<meta charset="utf-8">
<title>Lessons to Carry – Wallet Card</title>
<link href="https://fonts.googleapis.com/css2?family=Inconsolata:wght@400;600;700&display=swap" rel="stylesheet">
<style>
  :root {
    --stage: #202020;
    --ink: #0d0d0d;
    --orange: #f28c28;
    --gray: #b9b9b9;
    --white: #ffffff;
    --card-w: 900px;
    --card-h: 514px;
  }
  * { box-sizing: border-box; margin: 0; padding: 0; }
  html, body {
    width: 1200px; height: 1200px; overflow: hidden;
    background: var(--stage);
    font-family: "Inconsolata", "Consolas", monospace;
  }
  .stage {
    width: 1200px; height: 1200px;
    display: flex; flex-direction: column; align-items: center; justify-content: center;
    gap: 52px;
  }
  .card {
    position: relative;
    width: var(--card-w); height: var(--card-h);
    border-radius: 26px; overflow: hidden;
    display: flex; flex-direction: column;
  }
  .band-dark { background: var(--ink); color: var(--white); position: relative; }
  .band-orange { background: var(--orange); color: var(--ink); position: relative; }
  .divider { height: 8px; background: var(--gray); flex: none; }

  /* Front */
  .front .band-dark { height: 284px; padding: 22px 40px 0; }
  .front .band-orange { flex: 1; padding: 20px 40px 0; }
  .site { position: absolute; top: 18px; right: 40px; font-size: 17px; color: var(--white); }
  .title {
    text-align: center; color: var(--orange); font-weight: 700;
    font-size: 34px; letter-spacing: 3px; margin-top: 42px;
  }
  .subtitle { color: var(--orange); font-size: 22px; margin-top: 18px; }
  .compass { display: flex; gap: 44px; margin-top: 12px; font-size: 21px; }
  .rule-group { display: flex; gap: 12px; }
  .rule-label { color: var(--orange); font-weight: 700; }
  .rule-list { list-style: none; line-height: 1.35; }
  .rule-list li::before { content: "• "; color: var(--orange); }
  .poem { font-size: 20px; line-height: 1.32; color: var(--white); }
  .poem ul { list-style: none; margin-top: 2px; }
  .poem li::before { content: "• "; }
  .poem-credit { position: absolute; right: 120px; top: 78px; font-size: 16px; color: var(--ink); }
  .motto { text-align: center; font-size: 21px; color: var(--white); margin-top: 18px; }
  .motto cite { font-style: normal; font-size: 15px; margin-left: 8px; }

  /* Back */
  .back .band-orange { height: 250px; padding: 44px 40px 0; }
  .back .band-dark { flex: 1; padding: 26px 40px 0; }
  .creed-title { font-weight: 700; font-size: 22px; margin-bottom: 10px; }
  .creed { list-style: none; font-size: 19px; line-height: 1.42; }
  .creed li::before { content: "• "; }
  .pledge { margin-left: 400px; font-size: 18px; line-height: 1.35; }
  .pledge-title { color: var(--orange); font-weight: 700; margin-bottom: 4px; }
  .sign { display: flex; flex-direction: column; align-items: center; gap: 10px; margin-top: 14px; width: 150px; margin-left: 110px; }
  .sign span { width: 100%; border-top: 1px solid var(--gray); font-size: 11px; color: var(--gray); text-align: center; padding-top: 2px; }
  .live { position: absolute; left: 40px; bottom: 22px; font-size: 20px; }
  .live-lead { color: var(--orange); margin-bottom: 8px; margin-left: 60px; }
  .values { display: flex; gap: 14px; color: var(--orange); }
  .values .dot { color: var(--white); }
</style>
</head>
<body>
<main class="stage">

  <section class="card front" aria-label="Card front">
    <div class="band-dark">
      <p class="site">www.brightpathcourts.com</p>
      <h1 class="title">LESSONS TO CARRY</h1>
      <h2 class="subtitle">The Golden Compass of Growth</h2>
      <div class="compass">
        <div class="rule-group">
          <span class="rule-label">NEVER</span>
          <ul class="rule-list"><li>Lie</li><li>Cheat</li><li>Steal</li></ul>
        </div>
        <div class="rule-group">
          <span class="rule-label">DON'T</span>
          <ul class="rule-list"><li>Blame</li><li>Complain</li><li>Give Up</li></ul>
        </div>
        <div class="rule-group">
          <span class="rule-label">ALWAYS</span>
          <ul class="rule-list"><li>Be Grateful</li><li>Uplift Others</li><li>Do More Than Your Share</li></ul>
        </div>
      </div>
    </div>
    <div class="divider"></div>
    <div class="band-orange">
      <div class="poem">
        <p>Four things a man must learn to do<br>If he would make his life more true:</p>
        <ul>
          <li>To think without confusion clearly,</li>
          <li>To love his fellow man sincerely,</li>
          <li>To act from honest motives purely,</li>
          <li>To trust in God and Heaven securely.</li>
        </ul>
      </div>
      <p class="poem-credit">Henry Lanford</p>
      <p class="motto">“Make each day your masterpiece.” <cite>Coach Dale Whitmore</cite></p>
    </div>
  </section>

  <section class="card back" aria-label="Card back">
    <div class="band-orange">
      <h2 class="creed-title">A 5-Point Creed</h2>
      <ul class="creed">
        <li>Be intentional to grow and learn one thing each day.</li>
        <li>Honour others in everything you say and do.</li>
        <li>Act with integrity and uprightness in all matters.</li>
        <li>Prioritize serving and giving to others above yourself.</li>
        <li>Dream, pray, and expect for the impossible.</li>
      </ul>
    </div>
    <div class="divider"></div>
    <div class="band-dark">
      <div class="pledge">
        <p class="pledge-title">Golden Compass &amp; 5-Point Creed Pledge:</p>
        <p>I commit to doing my best to live out the Golden Compass and 5-Point Creed each day.</p>
        <div class="sign"><span>Signature</span><span>Date</span></div>
      </div>
      <div class="live">
        <p class="live-lead">Live every day with:</p>
        <p class="values">
          <span>Passion</span><span class="dot">•</span><span>Wonder</span><span class="dot">•</span><span>Playfulness</span><span class="dot">•</span><span>Gratitude</span><span class="dot">•</span><span>Love</span>
        </p>
      </div>
    </div>
  </section>

</main>
</body>
</html>
```